Gestaltung einer Webseite für Eventfotografie
pixelquarz hat hervorragende Arbeit geleistet. Das Design ist 1A, sowie die weitere Projektabwicklung, völlig problemlos, sehr freundlich, entgegenkommend und kompetent. Ich kann pixelquarz jederzeit mit 5 Sternen als Designer weiterempfehlen! hubertus
Zielgruppe
Eventagenturen, Entscheider in Marketing- bzw. Eventabteilungen von mittelständischen oder großen Firmen sowie Bankettabteilungen von Hotels.
Aufgabenstellung
Neuerstellung Webseitenlayout und programmtechnische Umsetzung einer Webseite.
Die Webseite soll "Der Momentrahmen"heissen. Die Wörter "Der Momentrahmen" wären grafisch dementsprechend auch zu gestalten.
Die Webseite dient als Schaufenster zur Generierung von Anfragen / Aufträgen die Eventfotografie betreffend. Da der erste Eindruck entscheidend ist, stelle ich mir beim Aufruf der Webseite vor, dass prominent 3-5 Fotos erscheinen. Die Animation der Fotos soll so gestaltet sein, als wenn man Papierabzüge auf einen Tisch legt (Mein Haus, Mein Pferd, mein Boot...)
Darüber hinaus sollen weitere weniger auffällige Eventfotos erscheinen.
Es sollen eine Homepage, eine Kontaktseite, eine Fotogalerieseite, eine Referenzseite (mit Kundennamen und Fotos) und evtl. ein Onlinekalender integriert sein, auf dem der Benutzer das Eventdatum anklicken und seine Anfrage platzieren kann. Impressum ist obligatorisch.
Alle Bereiche sollen übersichtlich und klar gestaltet sein, so dass sich der User schnell orientieren kann.
Auf jeder Unterseite soll ein ca. 5DM-Stück grosser auffälliger "Termin-Anfrage"-Button platziert sein.

```html
<!DOCTYPE html>
<html lang="de">
<head>
<meta charset="utf-8">
<title>Der Momentrahmen – Eventfotografie</title>
<link rel="stylesheet" href="https://fonts.googleapis.com/css2?family=Arimo:wght@400;700&display=swap">
<style>
  :root {
    --pink: #e0005e;
    --grey-light: #d6d6d6;
    --grey-mid: #a9a9a9;
    --grey-dark: #8a8a8a;
    --white: #ffffff;
    --ink: #111111;
    --photo-dark: #1b1b1d;
    --photo-mid: #5a5a5e;
  }
  * { box-sizing: border-box; margin: 0; padding: 0; }
  html, body { width: 1200px; height: 1172px; overflow: hidden; }
  body {
    position: relative;
    font-family: "Arimo", Arial, sans-serif;
    color: var(--ink);
    background: radial-gradient(ellipse at 50% 40%, var(--grey-light) 0%, var(--grey-mid) 70%, var(--grey-dark) 100%);
  }
  .logo {
    position: absolute; left: 57px; top: 12px;
    width: 140px; height: 140px; border-radius: 50%;
    background: var(--white);
    display: flex; flex-direction: column; align-items: center; justify-content: center;
  }
  .logo-name {
    font-size: 19px; font-weight: 400; line-height: 1.15;
    color: var(--ink); text-align: center; white-space: nowrap;
  }
  .main-nav { position: absolute; left: 638px; top: 59px; width: 385px; }
  .nav-bar { display: flex; height: 7px; }
  .nav-bar span { flex: 1; background: var(--white); margin-right: 1px; }
  .nav-bar span:last-child { margin-right: 0; }
  .nav-bar span.active { background: var(--pink); }
  .nav-links { display: flex; list-style: none; margin-top: 12px; }
  .nav-links li { flex: 1; text-align: right; font-size: 15px; font-weight: 700; color: var(--white); }
  .nav-links li.active { color: var(--pink); }
  .appointment-ribbon { position: absolute; right: 0; top: 0; }
  .slider-dots { position: absolute; left: 0; top: 0; }
  .photo { position: absolute; }
  .photo-main {
    left: 176px; top: 188px; width: 847px; height: 477px;
    background: linear-gradient(180deg, var(--photo-dark) 0%, #2c2c30 45%, #cfcfcf 80%, #e8e8e8 100%);
    box-shadow: 0 30px 30px -12px rgba(0,0,0,0.55);
  }
  .photo-side { top: 311px; width: 177px; height: 294px; opacity: 0.85; }
  .photo-left { left: 0; background: linear-gradient(90deg, #2a2e36, var(--photo-mid)); }
  .photo-right { left: 1023px; background: linear-gradient(90deg, #4a4a4e, #2a2024); }
  .slider-arrow { position: absolute; top: 619px; }
  .features {
    position: absolute; left: 0; top: 770px; width: 1200px; height: 227px;
    background: var(--white);
  }
  .feature { position: absolute; top: 32px; width: 345px; }
  .feature h2 { font-size: 19.5px; font-weight: 700; color: var(--pink); line-height: 1.2; }
  .feature p { margin-top: 36px; font-size: 15px; line-height: 17.6px; }
  .footer-links { position: absolute; top: 1122px; display: flex; align-items: center; }
  .footer-links svg { margin-right: 12px; }
  .footer-links span { font-size: 14px; font-weight: 700; color: var(--white); }
</style>
</head>
<body>
  <header>
    <div class="logo">
      <div class="logo-name">Der<br>Momentrahmen</div>
    </div>

    <nav class="main-nav">
      <div class="nav-bar"><span class="active"></span><span></span><span></span></div>
      <ul class="nav-links">
        <li class="active">Startseite</li>
        <li>Galerie</li>
        <li>Portfolio</li>
      </ul>
    </nav>

    <svg class="appointment-ribbon" width="139" height="135" viewBox="0 0 139 135">
      <polygon points="0,0 139,0 139,135" fill="var(--pink)"/>
      <g transform="translate(98,42) rotate(45)" fill="var(--white)" font-family="Arimo, Arial, sans-serif" font-size="14" text-anchor="middle">
        <text x="0" y="-4">TERMIN</text>
        <text x="0" y="13">vereinbaren</text>
      </g>
    </svg>
  </header>

  <svg class="slider-dots" width="1200" height="200">
    <circle cx="551" cy="164" r="11" fill="var(--pink)"/>
    <circle cx="586" cy="164" r="5.5" fill="var(--ink)"/>
    <circle cx="621" cy="164" r="5.5" fill="var(--ink)"/>
    <circle cx="657" cy="164" r="5.5" fill="var(--ink)"/>
  </svg>

  <section class="slider">
    <div class="photo photo-side photo-left" role="img" aria-label="Eventfoto: Ausstellungswand mit Modefotografie"></div>
    <div class="photo photo-side photo-right" role="img" aria-label="Eventfoto: Gäste bei einer Fahrzeugpräsentation"></div>
    <div class="photo photo-main" role="img" aria-label="Eventfoto: Gäste auf weißen Sofas in einer Fotoausstellung"></div>

    <svg class="slider-arrow" style="left:169px" width="53" height="52" viewBox="0 0 53 52">
      <polygon points="0,0 53,52 0,52" fill="var(--pink)"/>
      <path d="M8 36 h12 M8 36 l5 -4 M8 36 l5 4" stroke="var(--white)" stroke-width="3" fill="none"/>
    </svg>
    <svg class="slider-arrow" style="left:979px" width="53" height="52" viewBox="0 0 53 52">
      <polygon points="53,0 53,52 0,52" fill="var(--pink)"/>
      <path d="M33 36 h12 M45 36 l-5 -4 M45 36 l-5 4" stroke="var(--white)" stroke-width="3" fill="none"/>
    </svg>
  </section>

  <section class="features">
    <article class="feature" style="left:57px">
      <h2>PROFESSIONELLE FOTOGRAFIE</h2>
      <p>Lorem ipsum dolor sit amet, consetetur sadipscing elitr, sed diam nonumy eirmod tempor invidunt ut labore et dolore magna aliquyam erat, sed diam voluptua.<br>At vero eos et accusam et justo duo dolores et ea rebum.</p>
    </article>
    <article class="feature" style="left:430px">
      <h2>QUALITATIVE BILDBEARBEITUNG</h2>
      <p>Lorem ipsum dolor sit amet, consetetur sadipscing elitr, sed diam nonumy eirmod tempor invidunt ut labore et dolore magna aliquyam erat, sed diam voluptua. At vero eos et accusam et justo duo dolores et ea rebum.</p>
    </article>
    <article class="feature" style="left:804px">
      <h2>TOP PREIS-LEISTUNG</h2>
      <p>Lorem ipsum dolor sit amet, consetetur sadipscing elitr.<br>Sed diam nonumy eirmod tempor invidunt ut labore et dolore magna aliquyam erat, sed diam voluptua. At vero eos et accusam et justo duo dolores et ea rebum</p>
    </article>
  </section>

  <footer>
    <div class="footer-links" style="left:804px">
      <svg width="66" height="18"><circle cx="9" cy="9" r="8.5" fill="var(--pink)"/><circle cx="33" cy="9" r="8.5" fill="var(--white)"/><circle cx="57" cy="9" r="8.5" fill="var(--white)"/></svg>
      <span>Impressum</span>
    </div>
    <div class="footer-links" style="left:1002px">
      <svg width="66" height="18"><circle cx="9" cy="9" r="8.5" fill="var(--pink)"/><circle cx="33" cy="9" r="8.5" fill="var(--white)"/><circle cx="57" cy="9" r="8.5" fill="var(--white)"/></svg>
      <span>Kontakt</span>
    </div>
  </footer>
</body>
</html>
```